Brindle School of Music Website Design

Brindle School of Music would like to have a website designed. They are a new business similar to Halvern (https://halvernmusic.example).

We prefer using Adobe Fonts throughout the design. Kepler was used for the logo. Lorem Ipsum is fine to use except for headers.

Please keep track of any images/icons that are used in your design. We plan on purchasing the images used in the winning design.

Target Market(s)

Children age 10 - 18

Number of Pages Required

1 page

Font styles to use
Sans Serif

Colors
0054AA
0677BA
7BADD7
CADEEF
E8F1F8

```html
<!DOCTYPE html>
<html lang="en">
<head>
<meta charset="utf-8">
<title>Brindle School of Music</title>
<link href="https://fonts.googleapis.com/css2?family=Playfair+Display:wght@700&family=Roboto:wght@400;500;700&display=swap" rel="stylesheet">
<style>
:root{
  --blue:#0054AA;
  --blue-mid:#0677BA;
  --blue-light:#7BADD7;
  --blue-pale:#CADEEF;
  --blue-wash:#E8F1F8;
  --navy:#0b1d3f;
  --ink:#222;
  --text:#444;
  --grey:#efefef;
  --white:#fff;
}
*{box-sizing:border-box;margin:0;padding:0}
html,body{width:1200px;height:4082px;overflow:hidden}
body{position:relative;font-family:'Roboto',sans-serif;color:var(--text);background:var(--white)}
.abs{position:absolute}
.serif{font-family:'Playfair Display',serif;font-weight:700;letter-spacing:-.5px}
.btn{position:absolute;display:flex;align-items:center;justify-content:center;gap:12px;background:var(--blue);color:var(--white);font-weight:700;font-size:16px;text-transform:uppercase}
.btn svg{width:16px;height:16px}
.photo{position:absolute}

/* header */
.topline{top:0;left:0;width:1200px;height:5px;background:var(--blue)}
.utility{top:20px;left:686px;display:flex;gap:34px;font-size:15px;font-weight:500;color:var(--ink);letter-spacing:.5px}
.utility span{display:flex;align-items:center;gap:10px}
.utility svg{width:14px;height:14px}
.head-btn{top:55px;height:40px;font-size:15px;gap:10px}
.navbar{top:106px;left:0;width:1200px;height:48px;background:var(--blue)}
.nav{top:106px;left:307px;height:48px;display:flex;align-items:center;gap:0;color:var(--white);font-size:16px}
.nav span{padding:0 26px;position:relative}
.nav span+span::before{content:"|";position:absolute;left:-4px}
.brand-box{top:5px;left:113px;width:160px;height:149px;background:var(--white);display:flex;flex-direction:column;align-items:center;justify-content:flex-end;padding-bottom:8px}
.brand-mark{width:62px;height:62px;border-radius:50%;background:var(--blue);margin-bottom:8px}
.brand-name{font-weight:700;color:var(--blue);text-align:center;line-height:1.1}
.brand-name .big{display:block;font-size:25px}
.brand-name .small{display:block;font-size:10px}

/* hero */
.hero{top:154px;left:0;width:1200px;height:596px;background:linear-gradient(90deg,#f1f1f1 0%,#e6e6e6 32%,#b48a62 55%,#6b4a35 75%,#3a2b24 100%)}
.hero-kicker{top:348px;left:117px;font-size:38px;color:var(--blue)}
.hero-title{top:408px;left:115px;font-size:60px;line-height:66px;color:var(--ink);text-transform:uppercase}
.arrow{width:38px;height:38px;border-radius:50%;display:flex;align-items:center;justify-content:center}

/* intro */
.intro{top:750px;left:0;width:1200px;height:245px;background:var(--blue);color:var(--white);text-align:center}
.intro h2{position:absolute;top:58px;width:100%;font-size:26px;text-transform:uppercase}
.intro p{position:absolute;top:114px;left:185px;width:830px;font-size:15px;line-height:26px}

.section-title{position:absolute;width:1200px;text-align:center;font-size:26px;text-transform:uppercase;color:var(--navy)}

/* programs */
.program{position:absolute;top:1135px;width:250px;text-align:center}
.program .circle{width:194px;height:194px;border-radius:50%;margin:0 auto}
.program h3{margin-top:22px;font-size:15px;font-weight:700;color:var(--ink);letter-spacing:.3px}
.program p{margin-top:12px;font-size:15px;font-weight:700;color:var(--blue)}

/* about */
.about{top:1482px;left:0;width:1200px;height:515px;background:var(--grey)}
.about-frame{top:1545px;left:114px;width:428px;height:389px;background:#bbb;border-radius:4px;padding:9px}
.about-frame div{width:100%;height:100%;background:linear-gradient(135deg,#d7c7b6,#7f8fa6 55%,#c8a03a 85%)}
.body-text{font-size:15px;line-height:25.7px;color:var(--text);text-align:justify}

/* events */
.events{top:2592px;left:0;width:1200px;height:546px;background:linear-gradient(135deg,#163889,#2b4aa6 50%,#1c3a92)}
.card{position:absolute;top:2842px;width:302px;height:212px;background:var(--white)}
.card-img{position:absolute;top:2745px;width:280px;height:197px}
.card-date{position:absolute;top:131px;left:33px;font-family:'Playfair Display',serif;font-size:13px;color:var(--blue);display:flex;gap:10px;align-items:center}
.card-date svg{width:14px;height:14px}
.card-title{position:absolute;top:156px;left:33px;width:255px;font-size:15.5px;font-weight:700;line-height:25px;color:var(--ink)}

/* partners */
.partner{position:absolute;width:152px;height:79px;border:1px solid #e3e3e3;background:var(--white);display:flex;align-items:center;justify-content:center}
.partner i{display:block;width:70px;height:26px;border-radius:13px;background:var(--blue-pale)}

/* footer */
.footer{top:3614px;left:0;width:1200px;height:396px;background:var(--navy)}
.foot-brand{top:3808px;left:94px;width:240px;text-align:center;color:var(--white);font-weight:700;line-height:1.1}
.foot-brand .big{display:block;font-size:38px}
.foot-brand .small{display:block;font-size:15px;margin-top:2px;letter-spacing:.5px}
.foot-head{position:absolute;top:3683px;font-size:14px;font-weight:700;color:var(--white)}
.foot-list{position:absolute;top:3730px;list-style:none;font-size:15px;color:var(--white)}
.foot-list li{height:38.5px;display:flex;gap:14px}
.foot-list li::before{content:"»"}
.contact{position:absolute;left:819px;display:flex;align-items:center;gap:14px;font-size:15px;color:var(--white);line-height:24px}
.contact .dot{width:37px;height:37px;border-radius:50%;background:var(--blue);display:flex;align-items:center;justify-content:center;flex:none}
.contact svg{width:15px;height:15px}
.social{position:absolute;top:3916px;width:31px;height:31px;border:1px solid var(--white)}
.bottom{top:4010px;left:0;width:1200px;height:72px;background:var(--blue);color:var(--white);font-size:14px;display:flex;align-items:center;justify-content:center}
</style>
</head>
<body>

<!-- header -->
<div class="abs topline"></div>
<div class="abs utility">
  <span><svg viewBox="0 0 16 16"><circle cx="8" cy="8" r="7" fill="#222"/><path d="M1 8h14M8 1c3 3 3 11 0 14M8 1c-3 3-3 11 0 14" stroke="#fff" fill="none"/></svg>LANGUAGE</span>
  <span><svg viewBox="0 0 16 16"><circle cx="6.5" cy="6.5" r="5" stroke="#222" stroke-width="2" fill="none"/><path d="M10 10l5 5" stroke="#222" stroke-width="2.4"/></svg>SEARCH</span>
  <span><svg viewBox="0 0 16 16"><circle cx="8" cy="4.5" r="3.5" fill="#222"/><path d="M1 16c0-5 3-7 7-7s7 2 7 7z" fill="#222"/></svg>MY ACCOUNT</span>
</div>
<div class="btn head-btn" style="left:823px;width:136px">REGISTER <svg viewBox="0 0 16 16"><circle cx="8" cy="8" r="8" fill="#fff"/><path d="M6 4l4 4-4 4" stroke="#0054AA" stroke-width="2.2" fill="none"/></svg></div>
<div class="btn head-btn" style="left:969px;width:118px">DONATE <svg viewBox="0 0 16 16"><path d="M8 15L1.5 8.5A4 4 0 018 3a4 4 0 016.5 5.5z" fill="#fff"/></svg></div>
<div class="abs navbar"></div>
<div class="abs nav"><span>HOME</span><span>ABOUT US</span><span>OUR PROGRAMS</span><span>STUDENT RESOURCES</span><span>CONTACT US</span></div>
<div class="abs brand-box">
  <div class="brand-mark"></div>
  <div class="brand-name"><span class="big">BRINDLE</span><span class="small">SCHOOL OF MUSIC</span></div>
</div>

<!-- hero -->
<div class="photo hero" role="img" aria-label="Teacher and child playing piano together"></div>
<div class="abs serif hero-kicker">WELCOME TO</div>
<div class="abs serif hero-title">Brindle School<br>of Music</div>
<div class="btn" style="top:567px;left:117px;width:201px;height:59px">GET STARTED <svg viewBox="0 0 16 16"><circle cx="8" cy="8" r="8" fill="#fff"/><path d="M6 4l4 4-4 4" stroke="#0054AA" stroke-width="2.2" fill="none"/></svg></div>
<div class="abs arrow" style="top:471px;left:37px;background:#bfbfbf"><svg width="14" height="14" viewBox="0 0 14 14"><path d="M9 2L4 7l5 5" stroke="#222" stroke-width="2" fill="none"/></svg></div>
<div class="abs arrow" style="top:471px;left:1124px;background:var(--blue)"><svg width="14" height="14" viewBox="0 0 14 14"><path d="M5 2l5 5-5 5" stroke="#fff" stroke-width="2" fill="none"/></svg></div>

<!-- intro -->
<section class="abs intro">
  <h2 class="serif">Brindle School of Music</h2>
  <p>Lorem ipsum dolor sit amet, consectetur adipiscing elit. Nunc lacinia neque eu nisl rutrum blandit. Sed eted metus id nibh dictum rutrum id eget nisl. Suspendisse bibendum tortor sit amet purus tristique hendreried Integer maximus sited amet justo eget fermentum. Nulla nec dui maximus metus congue vulputate.Morbi in imperdiet nulla.</p>
</section>

<!-- programs -->
<h2 class="section-title serif" style="top:1076px">Our Programs</h2>
<div class="program" style="left:94px"><div class="circle" style="background:radial-gradient(circle,#c9a25a,#8a4a2e 60%,#5a3324)" role="img" aria-label="Children playing brass and string instruments"></div><h3>LOREM IPSUM DOLOR SIT</h3><p>Ages 4+</p></div>
<div class="program" style="left:347px"><div class="circle" style="background:radial-gradient(circle,#d8c7bb,#6f5a52 60%,#2d2a2a)" role="img" aria-label="Student playing a keyboard"></div><h3>LOREM IPSUM DOLOR SIT</h3><p>Newborns-8 Years</p></div>
<div class="program" style="left:601px"><div class="circle" style="background:radial-gradient(circle,#8c8a86,#3d3b3a 60%,#1d1d1f)" role="img" aria-label="Guitarist recording in a studio"></div><h3>LOREM IPSUM DOLOR SIT</h3><p>Ages 18 +</p></div>
<div class="program" style="left:855px"><div class="circle" style="background:radial-gradient(circle,#b9c3cc,#5e6a78 60%,#2b3340)" role="img" aria-label="Producer working at a mixing desk"></div><h3>LOREM IPSUM DOLOR SIT</h3><p>All ages.all tuition-free</p></div>

<!-- about -->
<div class="abs about"></div>
<div class="abs about-frame"><div role="img" aria-label="Music therapist playing guitar with a student"></div></div>
<h2 class="abs serif" style="top:1549px;left:631px;font-size:26px;color:var(--navy)">ABOUT US</h2>
<p class="abs body-text" style="top:1594px;left:631px;width:456px">Lorem ipsum dolor sit&nbsp; consectetur adipiscing elit. Nunc lacinia neque eu nisl rutrum blandit. Sed et metus id nibh dictum rutrum id eget nisl. Suspendisse bibendum tortor sit amet purus tristique hendrerit. Integer maximus sit amet justo eget fermentum. Nulla nec dui maximus metus congue vulputate. Proin ac semper nunc. Morbi in imperdiet nulla. Morbi quam sapien, tristique ac enim vel, pulvinar elementum massa. scelerisque convallis augue. Aliquam cursus ornare nibh non fringilla. Phasellus dapibus eros et luctus luctus. Donec cursus nisl enim, vel tempus mauris semper laoreet. Donec euismod finibus consequat Donec consequat</p>
<div class="btn" style="top:1873px;left:631px;width:162px;height:53px;font-size:15px">LEARN MORE <svg viewBox="0 0 16 16"><circle cx="8" cy="8" r="8" fill="#fff"/><path d="M6 4l4 4-4 4" stroke="#0054AA" stroke-width="2.2" fill="none"/></svg></div>

<!-- gift -->
<div class="photo" style="top:2092px;left:591px;width:574px;height:500px;background:radial-gradient(ellipse at 60% 55%,#b8612e 0%,#d9b44a 35%,rgba(255,255,255,0) 70%)" role="img" aria-label="Young man playing the cello"></div>
<h2 class="section-title serif" style="top:2078px">Give the Gift of Music</h2>
<p class="abs body-text" style="top:2161px;left:127px;width:428px;font-size:14.6px;letter-spacing:-.1px">Lorem ipsum dolor sit&nbsp; consectetur adipiscing elit. Nunc lacinia neque eu nisl rutrum blandit. Sed et metus id nibh dictum rutrum id eget nisl. Suspendisse bibendum tortor sit amet purus tristique hendrerit. Integer maximus sit amet justo eget fermentum. Nulla nec dui maximus metus congue vulputate. Proin ac semper nunc. Morbi in imperdiet nulla. Morbi quam sapien, tristique enim pulvinar elementum massa. scelerisque convallis augue. Aliquam cursus ornare nibh non fringilla. Phasellus dapibus eros et luctus luctus. Donec cursus</p>
<div class="btn" style="top:2414px;left:127px;width:162px;height:53px;font-size:15px">LEARN MORE <svg viewBox="0 0 16 16"><circle cx="8" cy="8" r="8" fill="#fff"/><path d="M6 4l4 4-4 4" stroke="#0054AA" stroke-width="2.2" fill="none"/></svg></div>

<!-- events -->
<div class="abs events"></div>
<h2 class="section-title serif" style="top:2666px;color:var(--white)">Our Events</h2>
<div class="card" style="left:109px"><div class="card-date"><svg viewBox="0 0 14 14"><rect x="1" y="2" width="12" height="11" fill="none" stroke="#0054AA" stroke-width="1.6"/><path d="M1 5h12M4 0v3M10 0v3" stroke="#0054AA" stroke-width="1.6"/></svg>16.1.2023</div><div class="card-title">Lorem ipsum dolor sit consectetur adipiscing Integer pretium eu ante</div></div>
<div class="card" style="left:447px"><div class="card-date"><svg viewBox="0 0 14 14"><rect x="1" y="2" width="12" height="11" fill="none" stroke="#0054AA" stroke-width="1.6"/><path d="M1 5h12M4 0v3M10 0v3" stroke="#0054AA" stroke-width="1.6"/></svg>16.1.2023</div><div class="card-title">Lorem ipsum dolor sit consectetur adipiscing Integer pretium eu ante</div></div>
<div class="card" style="left:786px"><div class="card-date"><svg viewBox="0 0 14 14"><rect x="1" y="2" width="12" height="11" fill="none" stroke="#0054AA" stroke-width="1.6"/><path d="M1 5h12M4 0v3M10 0v3" stroke="#0054AA" stroke-width="1.6"/></svg>16.1.2023</div><div class="card-title">Lorem ipsum dolor sit consectetur adipiscing Integer pretium eu ante</div></div>
<div class="card-img" style="left:120px;background:linear-gradient(135deg,#e2a13a,#9b5a2c 50%,#d8d0c8)" role="img" aria-label="Teacher guiding a child on guitar"></div>
<div class="card-img" style="left:458px;background:linear-gradient(135deg,#e8e4dc,#c7a88c 50%,#2a2a2a)" role="img" aria-label="Children gathered around a piano"></div>
<div class="card-img" style="left:797px;background:linear-gradient(135deg,#8e98a8,#c7a46e 50%,#6b4a2e)" role="img" aria-label="Close-up of hands on an acoustic guitar"></div>

<!-- partners -->
<h2 class="section-title serif" style="top:3208px">Featured Partners</h2>
<p class="abs" style="top:3262px;left:150px;width:900px;text-align:center;font-size:15px;line-height:25px">Lorem ipsum dolor sit amet consectetur adipiscing elit, sed do eiusmod tempor incididunt&nbsp; labore et dolore magna aliqua.<br>Ut enim ad minim veniam, quis nostrud exercitation ullamco laboris nisi ut aliquip ex ea commodo consequat.</p>
<div class="partner" style="top:3340px;left:114px"><i></i></div>
<div class="partner" style="top:3340px;left:277px"><i></i></div>
<div class="partner" style="top:3340px;left:441px"><i></i></div>
<div class="partner" style="top:3340px;left:605px"><i></i></div>
<div class="partner" style="top:3340px;left:769px"><i></i></div>
<div class="partner" style="top:3340px;left:933px"><i></i></div>
<div class="partner" style="top:3437px;left:114px"><i></i></div>
<div class="partner" style="top:3437px;left:277px"><i></i></div>
<div class="partner" style="top:3437px;left:441px;box-shadow:0 2px 10px rgba(0,0,0,.15)"><i></i></div>
<div class="partner" style="top:3437px;left:605px"><i></i></div>
<div class="partner" style="top:3437px;left:769px"><i></i></div>
<div class="partner" style="top:3437px;left:933px"><i></i></div>

<!-- footer -->
<div class="abs footer"></div>
<div class="abs" style="top:3690px;left:164px;width:100px;height:100px;border-radius:50%;background:var(--blue)"></div>
<div class="abs foot-brand"><span class="big">BRINDLE</span><span class="small">SCHOOL OF MUSIC</span></div>
<div class="social" style="left:136px" aria-label="Social link"></div>
<div class="social" style="left:178px" aria-label="Social link"></div>
<div class="social" style="left:220px" aria-label="Social link"></div>
<div class="social" style="left:262px" aria-label="Social link"></div>

<div class="foot-head" style="left:407px">QUICK LINKS</div>
<ul class="foot-list" style="left:407px"><li>Home</li><li>About Us</li><li>Our Programs</li><li>Student Resources</li><li>Contact Us</li></ul>
<div class="foot-head" style="left:615px">OTHER LINKS</div>
<ul class="foot-list" style="left:615px"><li>Team</li><li>FAQ</li><li>Terms Of Use</li><li>Privacy Policy</li><li>Help Services</li></ul>
<div class="foot-head" style="left:819px">ABOUT US</div>
<div class="contact" style="top:3734px"><span class="dot"><svg viewBox="0 0 16 16"><path d="M3 1l3 3-2 2c1 2 3 4 5 5l2-2 3 3-2 3C7 15 1 9 1 3z" fill="#fff"/></svg></span><b>+ 1 555 010 0100</b></div>
<div class="contact" style="top:3794px"><span class="dot"><svg viewBox="0 0 16 16"><rect x="1.5" y="3.5" width="13" height="9" rx="1" fill="none" stroke="#fff" stroke-width="1.6"/><path d="M2 4l6 5 6-5" stroke="#fff" stroke-width="1.6" fill="none"/></svg></span>info@brindleschoolofmusic.example</div>
<div class="contact" style="top:3855px"><span class="dot"><svg viewBox="0 0 16 16"><path d="M8 15s5-5 5-9A5 5 0 003 6c0 4 5 9 5 9z" fill="#fff"/><circle cx="8" cy="6" r="2" fill="#0054AA"/></svg></span>10090&nbsp; Lorem ipsum dolor amet,<br>consectetur adipiscing elit.</div>

<div class="abs bottom">© &nbsp;2023 Brindle school of music. All Right Reserved.</div>
</body>
</html>
```